NEW YORK Plumbing/utility company 10 year anniversary business card

Looking For simple back and front business card would like to include a few things in description
We offer 24/7 emergency service
residential
commercial
industrial
municipal
services offered
Plumbing
hydro excavation
hydro jetting
Well pumps
Sewer pumps
water mains
sewer mains

```html
<!DOCTYPE html>
<html lang="en">
<head>
<meta charset="utf-8">
<title>KRL Ridgeline Water &amp; Sewer — Business Card</title>
<link rel="stylesheet" href="https://fonts.googleapis.com/css2?family=Roboto:wght@400;500;700&display=swap">
<style>
  :root {
    --bg: #0c4f86;
    --brand-blue: #0f5c9e;
    --sky-blue: #35a3e3;
    --splash-light: #cfe8f8;
    --splash-mid: #8cc6ec;
    --card-white: #ffffff;
    --card-grey: #eef1f4;
    --back-top: #0b6bb0;
    --back-bottom: #0a4b86;
    --back-text: #e6f1fa;
  }
  * { box-sizing: border-box; margin: 0; padding: 0; }
  html, body { width: 1200px; height: 1000px; overflow: hidden; }
  body {
    background: var(--bg);
    font-family: "Roboto", Arial, sans-serif;
    position: relative;
  }
  .card {
    position: absolute;
    left: 250px;
    width: 700px;
    height: 400px;
    border-radius: 4px;
    overflow: hidden;
    box-shadow: 0 18px 40px rgba(0, 0, 0, 0.3);
  }

  /* Front */
  .card-front {
    top: 70px;
    background: linear-gradient(135deg, var(--card-white) 55%, var(--card-grey));
  }
  .splash-art {
    position: absolute;
    left: -40px;
    top: -30px;
    width: 230px;
    height: 260px;
    border-radius: 0 0 60% 40%;
    background: radial-gradient(circle at 35% 40%, var(--splash-mid), var(--splash-light) 60%, rgba(207, 232, 248, 0) 75%);
  }
  .brand {
    position: absolute;
    left: 230px;
    top: 70px;
    color: var(--brand-blue);
    font-weight: 700;
    text-align: center;
    width: 340px;
  }
  .brand-mark {
    display: flex;
    align-items: center;
    justify-content: center;
    gap: 18px;
    font-size: 96px;
    line-height: 1;
    letter-spacing: 2px;
  }
  .brand-square {
    width: 34px;
    height: 34px;
    background: var(--brand-blue);
    border-radius: 4px;
  }
  .brand-line {
    font-size: 36px;
    letter-spacing: 2px;
    margin-top: 8px;
  }
  .brand-sub {
    font-size: 24px;
    letter-spacing: 3px;
    margin-top: 6px;
  }
  .contact {
    position: absolute;
    left: 0;
    right: 0;
    bottom: 44px;
    display: flex;
    justify-content: center;
    align-items: center;
    gap: 36px;
    color: var(--brand-blue);
    font-size: 21px;
  }
  .contact-divider {
    width: 2px;
    height: 26px;
    background: var(--brand-blue);
  }

  /* Back */
  .card-back {
    top: 530px;
    background: linear-gradient(160deg, var(--back-top), var(--back-bottom));
    color: var(--back-text);
  }
  .drop-art {
    position: absolute;
    left: 250px;
    top: 60px;
    width: 230px;
    height: 290px;
    border-radius: 50% 50% 50% 50% / 35% 35% 65% 65%;
    background: radial-gradient(circle at 45% 55%, rgba(120, 190, 240, 0.35), rgba(60, 150, 220, 0.15) 60%, rgba(60, 150, 220, 0) 75%);
  }
  .emergency {
    position: absolute;
    left: 70px;
    top: 150px;
  }
  .services {
    position: absolute;
    left: 430px;
    top: 70px;
  }
  .block-title {
    font-weight: 700;
    font-size: 23px;
    line-height: 1.2;
    margin-bottom: 10px;
  }
  .block-list {
    list-style: none;
    font-size: 21px;
    line-height: 1.32;
  }
  .emergency .block-list li::before {
    content: "";
    display: inline-block;
    width: 7px;
    height: 7px;
    border-radius: 50%;
    background: var(--back-text);
    margin: 0 10px 3px 4px;
  }
  .services .block-list li::before {
    content: "";
    display: inline-block;
    border-left: 5px solid transparent;
    border-right: 5px solid transparent;
    border-top: 7px solid var(--back-text);
    margin: 0 12px 3px 4px;
  }
</style>
</head>
<body>
  <section class="card card-front" aria-label="Business card front">
    <div class="splash-art" role="img" aria-label="Light blue water splash illustration"></div>
    <div class="brand">
      <div class="brand-mark"><span class="brand-square"></span>KRL</div>
      <div class="brand-line">RIDGELINE</div>
      <div class="brand-sub">WATER &amp; SEWER</div>
    </div>
    <div class="contact">
      <span class="contact-phone">845-555-0182</span>
      <span class="contact-divider"></span>
      <span class="contact-email">info@KRLNY.com</span>
    </div>
  </section>

  <section class="card card-back" aria-label="Business card back">
    <div class="drop-art" role="img" aria-label="Faint water drop with splash illustration"></div>
    <div class="emergency">
      <h2 class="block-title">We offer 24/7<br>emergency service</h2>
      <ul class="block-list">
        <li>Residential</li>
        <li>Commercial</li>
        <li>Industrial</li>
        <li>Municipal</li>
      </ul>
    </div>
    <div class="services">
      <h2 class="block-title">Services Offered</h2>
      <ul class="block-list">
        <li>Plumbing</li>
        <li>Hydro excavation</li>
        <li>Hydro jetting</li>
        <li>Well pumps</li>
        <li>Sewer pumps</li>
        <li>Water mains</li>
        <li>Sewer mains</li>
      </ul>
    </div>
  </section>
</body>
</html>
```